New website for Pilates Studio

I need a new version of my website
http://brightcoreflow.biz/
I want an updated fresh look with an easier to read schedule that looks good on mobile phones as well as laptops.
Clean, simple, fresh and BOLD

Target Market(s)

All ages, genders and races

Coding

Number of Pages Required

Colors
9bcb3c

Requirements
Must have
• Photos that mostly use the real images from our studio. Browse our facebook page, website or ask me for high quality images

```html
<!DOCTYPE html>
<html lang="en">
<head>
<meta charset="utf-8">
<title>Bright Core Flow – Pilates Studio</title>
<link href="https://fonts.googleapis.com/css2?family=Open+Sans:wght@400;600;700;800&family=Oswald:wght@400;500&display=swap" rel="stylesheet">
<style>
:root{
  --green:#9bcb3c;
  --green-dark:#7fae25;
  --green-pale:#e4f1c6;
  --green-tint:#cfe59b;
  --ink:#2e2e2e;
  --dark:#2b2b2b;
  --darker:#1f1f1f;
  --grey:#666;
  --white:#fff;
}
*{margin:0;padding:0;box-sizing:border-box}
html,body{width:861px;height:1200px;overflow:hidden}
body{font-family:"Open Sans",Arial,sans-serif;color:var(--ink);background:var(--white);position:relative}
.abs{position:absolute}

/* header */
.brand{left:30px;top:14px;display:flex;align-items:center;gap:10px}
.brand-dot{width:34px;height:34px;border-radius:50%;background:var(--green)}
.brand-name{font-size:26px;font-weight:700;color:var(--green-dark);line-height:1}
.brand-sub{left:74px;top:46px;font-size:11px;color:var(--grey)}
.book{left:532px;top:6px;width:158px;height:30px;background:var(--green);color:#fff;font-weight:700;font-size:15px;display:flex;align-items:center;justify-content:center;border-radius:3px}
.phone{left:705px;top:12px;font-size:16px;font-weight:700;color:var(--ink);display:flex;gap:6px;align-items:center}
.nav{left:490px;top:48px;display:flex;font-size:11px;font-weight:600;text-transform:uppercase;white-space:nowrap}
.nav a{color:var(--ink);text-decoration:none;padding:8px 14px;white-space:nowrap}
.nav a.active{background:var(--green);color:#fff;padding:8px 18px}

/* hero */
.hero{left:0;top:88px;width:861px;height:292px;background:linear-gradient(135deg,#c9c2b4 0%,#a59c8e 45%,#7a7468 100%)}
.hero-title{left:0;width:861px;top:298px;text-align:center;font-family:"Oswald",sans-serif;font-size:24px;color:#fff;letter-spacing:.5px}
.hero-btn{left:370px;top:334px;width:121px;height:30px;background:var(--dark);color:#fff;font-family:"Oswald",sans-serif;font-size:13px;display:flex;align-items:center;justify-content:center}

/* intro */
.welcome{left:30px;top:396px;width:550px}
h2{font-size:20px;font-weight:700;color:var(--ink);margin-bottom:10px}
h2 span{color:var(--green-dark)}
.welcome p,.green p{font-size:10.5px;line-height:15px;color:#444;margin-bottom:10px}
.green{left:612px;top:396px;width:225px}
.green h2{color:var(--green-dark)}
.seal{float:left;width:72px;height:72px;border-radius:50%;background:var(--green-tint);border:3px solid var(--green);margin:2px 10px 6px 0}

/* rates */
.band{left:0;top:618px;width:861px;height:142px;background:var(--green)}
.band-bg{left:0;top:760px;width:861px;height:175px;background:var(--green-pale)}
.rates-tab{left:378px;top:618px;width:105px;height:18px;background:var(--dark);color:#fff;font-size:11px;font-weight:700;display:flex;align-items:center;justify-content:center}
.plan{top:640px;width:192px;height:282px;background:var(--dark);color:#fff;text-align:center;display:flex;flex-direction:column}
.plan.feature{background:var(--green-tint);color:var(--ink);border:2px solid var(--green-dark)}
.plan h3{font-family:"Oswald",sans-serif;font-weight:500;font-size:21px;padding-top:14px;height:54px}
.plan .price{font-family:"Oswald",sans-serif;font-size:44px;line-height:56px;height:56px}
.plan .price small{font-size:13px}
.plan .note{font-size:11px;line-height:16px;height:56px;padding:4px 12px}
.plan .spacer{height:40px}
.plan ul{list-style:none}
.plan li{font-size:13px;line-height:30px;border-top:1px solid rgba(255,255,255,.18)}
.plan.feature li{border-top:1px solid rgba(0,0,0,.12);background:#fff;margin:0 8px}
.stars{margin:auto 10px 10px;height:22px;line-height:22px;background:#fff;color:#f2b90f;font-size:13px;letter-spacing:3px;text-align:center}

/* footer */
.footer{left:0;top:935px;width:861px;height:265px;background:var(--dark);color:#ccc}
.flinks{left:30px;top:960px;font-size:11px;display:flex;gap:14px;color:#ddd}
.faddr{left:30px;top:992px;font-size:10px;line-height:15px;color:#bbb}
.fcontact{left:150px;top:997px;font-size:10px;color:#bbb;display:flex;gap:26px}
.badge-a{left:585px;top:955px;width:82px;height:82px;border-radius:50%;background:#3b6fb3}
.badge-b{left:702px;top:960px;width:130px;height:80px;background:#e9edf3}
.news{left:30px;top:1118px;display:flex;align-items:center;gap:10px;font-size:14px;color:#ddd}
.news .field{width:140px;height:22px;background:#fff;font-size:9px;color:#999;padding:5px 6px}
.news .go{width:22px;height:22px;background:var(--green)}
.copy{left:0;top:1168px;width:861px;height:32px;background:var(--darker);font-size:10px;color:#999;text-align:center;line-height:32px}
</style>
</head>
<body>
<header>
  <div class="abs brand"><span class="brand-dot"></span><span class="brand-name">Bright Core Flow</span></div>
  <div class="abs brand-sub">Pilates &amp; Movement Studio</div>
  <div class="abs book">Book Your Seat</div>
  <div class="abs phone">
    <svg width="13" height="13" viewBox="0 0 24 24"><path fill="#2e2e2e" d="M6.6 10.8a15.1 15.1 0 0 0 6.6 6.6l2.2-2.2c.3-.3.7-.4 1-.2 1.1.4 2.3.6 3.6.6.6 0 1 .4 1 1V20c0 .6-.4 1-1 1A17 17 0 0 1 3 4c0-.6.4-1 1-1h3.5c.6 0 1 .4 1 1 0 1.3.2 2.5.6 3.6.1.3 0 .7-.2 1z"/></svg>
    1 123-456-7890</div>
  <nav class="abs nav"><a class="active">Home</a><a>Schedule</a><a>Instructors</a><a>Contact Us</a></nav>
</header>

<section>
  <div class="abs hero" role="img" aria-label="Group fitness class stretching in a bright studio"></div>
  <div class="abs hero-title">ONE-ON-ONE FITNESS SESSION</div>
  <div class="abs hero-btn">GET STARTED</div>
</section>

<section class="abs welcome">
  <h2><span>Welcome</span> To Bright Core Flow</h2>
  <p>Bright Core Flow Pilates and Movement Studio, in the heart of Harbor Village, is a warm, inviting studio where students and teachers alike are supported and encouraged to discover and grow at an individual pace through the field of integrated movement.</p>
  <p>We offer one-on-one sessions, group reformer classes and mat classes.</p>
  <p>Our mission is to promote long-term emotional and physical health through joyful, integrated movement training and to inspire and nurture our clients to learn more deeply about themselves and connect with fellow students and the community.</p>
</section>

<section class="abs green">
  <h2>We're Green Certified!</h2>
  <div class="seal" role="img" aria-label="Green business certification seal"></div>
  <p>Join our community in creating a sustainable future. We enjoy the benefits of protecting our environment with daily practice: recycling, using efficient lighting, conserving water, use, and acting responsibly.</p>
</section>

<section>
  <div class="abs band"></div>
  <div class="abs band-bg"></div>
  <div class="abs rates-tab">OUR RATES</div>

  <div class="abs plan" style="left:178px">
    <h3>PRIVATE SESSIONS</h3>
    <div class="price">$75 <small>hour</small></div>
    <div class="spacer"></div>
    <ul><li>$280/4</li><li>$650/10</li><li>$1200/20</li></ul>
    <div class="stars">★★★★</div>
  </div>
  <div class="abs plan feature" style="left:370px">
    <h3>MAT CLASSES</h3>
    <div class="note">includes yoga, boot camp and barre class</div>
    <ul><li>$15 single class</li><li>$120/10</li><li>$200/20</li></ul>
    <div class="stars">★★★★</div>
  </div>
  <div class="abs plan" style="left:562px">
    <h3>GROUP REFORMER</h3>
    <div class="price">$35 <small>class</small></div>
    <div class="spacer"></div>
    <ul><li>$140/4</li><li>$290/10</li><li>$500/20</li></ul>
    <div class="stars">★★★★</div>
  </div>
</section>

<footer>
  <div class="abs footer"></div>
  <div class="abs flinks"><span>Home</span><span>|</span><span>Schedule</span><span>|</span><span>Instructors</span><span>|</span><span>Contact Us</span></div>
  <div class="abs faddr">412 Linden Lane<br>Harbor CA 90001</div>
  <div class="abs fcontact"><span>☎ 831-555-0142</span><span>✉ hello@brightcoreflow.biz</span></div>
  <div class="abs badge-a" role="img" aria-label="Award badge"></div>
  <div class="abs badge-b" role="img" aria-label="Certification badge"></div>
  <div class="abs news">Newsletter Signup <span class="field">Enter Your Email Address</span><span class="go"></span></div>
  <div class="abs copy">© 2015 Bright Core Flow Pilates · All rights reserved.</div>
</footer>
</body>
</html>
```